Business Image

I have recently had a new company logo made up and require some new business cards to go with it.

Target Market(s)

Developers & high worth clients.

Industry/Entity Type

Business

Contact Information for Business Card

The business is in the construction/management industry. It needs to be classy but have a industrial feel. I would like the business card to be a elegant presentation in itself.

Requirements
Must have
• Current logo & company name. Colouring needs to be the same as the current design also.
Nice to have
• A few different designs & presentations of single and double sided business cards.

```html
<!DOCTYPE html>
<html lang="en">
<head>
<meta charset="UTF-8">
<title>Meridian Build Group – Business Card</title>
<link rel="stylesheet" href="https://fonts.googleapis.com/css2?family=Libre+Baskerville:wght@700&family=Arimo:wght@400;700&display=swap">
<style>
  :root {
    --navy: #1f3557;
    --ink: #3b4049;
    --muted: #555b64;
    --card: #eef0f2;
    --card-edge: #d5d9de;
    --backdrop: #c9ccd0;
  }
  * { margin: 0; padding: 0; box-sizing: border-box; }
  html, body {
    width: 1200px;
    height: 969px;
    overflow: hidden;
    background: var(--backdrop);
  }
  .canvas {
    position: relative;
    width: 1200px;
    height: 969px;
  }
  .card {
    position: absolute;
    left: 100px;
    top: 197px;
    width: 1000px;
    height: 574px;
    background: linear-gradient(135deg, #f4f5f7 0%, var(--card) 55%, #e6e9ec 100%);
    border: 1px solid var(--card-edge);
    box-shadow: 0 12px 30px rgba(30, 40, 55, 0.18);
  }
  .brand {
    position: absolute;
    left: 74px;
    top: 62px;
  }
  .brand-name {
    font-family: "Libre Baskerville", Georgia, serif;
    font-weight: 700;
    font-size: 46px;
    line-height: 1;
    color: var(--navy);
    letter-spacing: 0.5px;
  }
  .brand-sub {
    margin-top: 6px;
    font-family: "Arimo", Arial, sans-serif;
    font-weight: 700;
    font-size: 20px;
    letter-spacing: 3.4px;
    color: var(--ink);
  }
  .accent-bar {
    position: absolute;
    left: 0;
    top: 200px;
    width: 17px;
    height: 66px;
    background: var(--navy);
  }
  .person {
    position: absolute;
    left: 74px;
    top: 200px;
  }
  .person-name {
    font-family: "Libre Baskerville", Georgia, serif;
    font-weight: 700;
    font-size: 31px;
    line-height: 1.15;
    color: var(--navy);
  }
  .person-title {
    margin-top: 2px;
    font-family: "Arimo", Arial, sans-serif;
    font-weight: 700;
    font-size: 25px;
    color: var(--ink);
  }
  .address {
    position: absolute;
    left: 74px;
    top: 292px;
    font-family: "Arimo", Arial, sans-serif;
    font-size: 23px;
    line-height: 1.16;
    color: var(--muted);
    font-style: normal;
  }
  .contacts {
    position: absolute;
    left: 74px;
    top: 368px;
    list-style: none;
    font-family: "Arimo", Arial, sans-serif;
    font-size: 22px;
    color: var(--muted);
  }
  .contacts li {
    display: flex;
    align-items: center;
    height: 32px;
  }
  .contacts svg {
    width: 20px;
    height: 20px;
    margin-right: 16px;
    fill: var(--ink);
    flex: none;
  }
  .logo-lockup {
    position: absolute;
    left: 505px;
    top: 15px;
    width: 470px;
    height: 544px;
    display: flex;
    flex-direction: column;
    align-items: center;
    justify-content: center;
    gap: 26px;
  }
  .logo-square {
    width: 96px;
    height: 96px;
    background: var(--navy);
  }
  .logo-name {
    font-family: "Libre Baskerville", Georgia, serif;
    font-weight: 700;
    font-size: 54px;
    color: var(--navy);
    letter-spacing: 2px;
  }
</style>
</head>
<body>
<main class="canvas">
  <section class="card">
    <header class="brand">
      <div class="brand-name">MERIDIAN</div>
      <div class="brand-sub">BUILD GROUP</div>
    </header>

    <div class="accent-bar"></div>

    <div class="person">
      <div class="person-name">DANIEL HART</div>
      <div class="person-title">CEO/FOUNDER</div>
    </div>

    <address class="address">
      1420 Harbor View Road<br>
      Fairbanks, Alaska 99701
    </address>

    <ul class="contacts">
      <li>
        <svg viewBox="0 0 24 24" aria-hidden="true"><path d="M6.6 10.8a15.1 15.1 0 0 0 6.6 6.6l2.2-2.2a1 1 0 0 1 1-.25 11.4 11.4 0 0 0 3.6.57 1 1 0 0 1 1 1V20a1 1 0 0 1-1 1A17 17 0 0 1 3 4a1 1 0 0 1 1-1h3.5a1 1 0 0 1 1 1c0 1.25.2 2.45.57 3.57a1 1 0 0 1-.25 1z"/></svg>
        555.210.4836
      </li>
      <li>
        <svg viewBox="0 0 24 24" aria-hidden="true"><path d="M7 1h10a2 2 0 0 1 2 2v18a2 2 0 0 1-2 2H7a2 2 0 0 1-2-2V3a2 2 0 0 1 2-2zm0 3v14h10V4zm5 15.2a1.2 1.2 0 1 0 0 2.4 1.2 1.2 0 0 0 0-2.4z"/></svg>
        555.374.9120
      </li>
      <li>
        <svg viewBox="0 0 24 24" aria-hidden="true"><path d="M6 2h9l3 3v4H6zM3 10h18a1 1 0 0 1 1 1v7a1 1 0 0 1-1 1h-3v3H6v-3H3a1 1 0 0 1-1-1v-7a1 1 0 0 1 1-1zm5 7v3h8v-3zm10-4.5a1 1 0 1 0 0 2 1 1 0 0 0 0-2z"/></svg>
        555.608.2751
      </li>
      <li>
        <svg viewBox="0 0 24 24" aria-hidden="true"><path d="M2 5h20v14H2zm2 2v.5l8 5 8-5V7zm0 2.8V17h16V9.8l-8 5z"/></svg>
        daniel@meridianbuild.com
      </li>
      <li>
        <svg viewBox="0 0 24 24" aria-hidden="true"><path d="M12 2a10 10 0 1 0 0 20 10 10 0 0 0 0-20zm6.9 6h-3a15 15 0 0 0-1.3-3.9A8 8 0 0 1 18.9 8zM12 4a13 13 0 0 1 1.9 4h-3.8A13 13 0 0 1 12 4zM4.3 14a8 8 0 0 1 0-4h3.4a16 16 0 0 0 0 4zm.8 2h3a15 15 0 0 0 1.3 3.9A8 8 0 0 1 5.1 16zm3-8h-3a8 8 0 0 1 4.3-3.9A15 15 0 0 0 8.1 8zM12 20a13 13 0 0 1-1.9-4h3.8A13 13 0 0 1 12 20zm2.3-6H9.7a14 14 0 0 1 0-4h4.6a14 14 0 0 1 0 4zm.3 5.9a15 15 0 0 0 1.3-3.9h3a8 8 0 0 1-4.3 3.9zm1.7-5.9a16 16 0 0 0 0-4h3.4a8 8 0 0 1 0 4z"/></svg>
        www.meridianbuild.com
      </li>
    </ul>

    <div class="logo-lockup">
      <div class="logo-square"></div>
      <div class="logo-name">MERIDIAN</div>
    </div>
  </section>
</main>
</body>
</html>
```